Business Card design which attached logo. Company is called Tailored Shield and main colours are Orange & Black.

Company specialises in Paint Protection and Detailing for supercars.

Details needed on business card:

Sales

Address: Unit 14, 227 Harlow Street, Fernmere Vale, NSW 2391

Phone: 02 8419 2753

website: www.tailoredshield.com.au

Email: sales@tailoredshield.com.au

```html
<!DOCTYPE html>
<html lang="en">
<head>
<meta charset="utf-8">
<title>Tailored Shield — Business Card</title>
<link rel="stylesheet" href="https://fonts.googleapis.com/css2?family=Raleway:wght@400;500&display=swap">
<style>
  :root {
    --backdrop: #d8d6d1;
    --card: #080808;
    --orange: #e0561d;
    --light: #d6d6d6;
    --muted: #b3b3b3;
  }
  * { box-sizing: border-box; margin: 0; padding: 0; }
  html, body { width: 1200px; height: 865px; overflow: hidden; }
  body {
    background: var(--backdrop);
    font-family: "Raleway", sans-serif;
    position: relative;
  }
  .card {
    position: absolute;
    width: 525px;
    height: 300px;
    background: var(--card);
    box-shadow: 0 10px 24px rgba(0,0,0,0.28);
  }
  .card--front { left: 60px; top: 120px; }
  .card--back { left: 615px; top: 445px; }

  .brand-name {
    color: var(--orange);
    font-weight: 400;
    letter-spacing: 0.04em;
    text-transform: uppercase;
    white-space: nowrap;
  }
  .card--front .brand-name {
    position: absolute; left: 0; right: 0; top: 112px;
    text-align: center; font-size: 26px;
  }
  .card--front .site {
    position: absolute; left: 0; right: 0; top: 168px;
    text-align: center; font-size: 13px; color: var(--light);
  }
  .site .accent, .contact .accent { color: var(--orange); }

  .card--back .brand-name--logo {
    position: absolute; left: 0; right: 0; top: 70px;
    text-align: center; font-size: 20px;
  }
  .identity {
    position: absolute; left: 40px; top: 196px; text-align: right; width: 210px;
  }
  .identity .brand-name { font-size: 19px; display: block; }
  .identity .role { font-size: 14px; color: var(--muted); margin-top: 3px; display: block; }
  .divider {
    position: absolute; left: 266px; top: 140px; width: 1px; height: 105px;
    background: var(--orange);
  }
  .contact {
    position: absolute; left: 280px; top: 140px;
    list-style: none; font-size: 11.5px; color: var(--light); line-height: 17px;
  }
  .contact li { display: flex; align-items: center; gap: 6px; white-space: nowrap; }
  .contact svg { width: 10px; height: 10px; flex: none; }
</style>
</head>
<body>
  <section class="card card--front">
    <span class="brand-name">Tailored Shield</span>
    <p class="site">www.<span class="accent">tailoredshield</span>.com.au</p>
  </section>

  <section class="card card--back">
    <span class="brand-name brand-name--logo">Tailored Shield</span>
    <div class="identity">
      <span class="brand-name">Tailored Shield</span>
      <span class="role">Founder &amp; CEO</span>
    </div>
    <div class="divider"></div>
    <ul class="contact">
      <li>Unit 14, 227 Harlow Street,</li>
      <li>Fernmere Vale, NSW 2391</li>
      <li>
        <svg viewBox="0 0 10 10" aria-hidden="true"><rect x="2" y="0.5" width="6" height="9" rx="1.2" fill="none" stroke="var(--orange)" stroke-width="1.4"/></svg>
        02 8419 2753
      </li>
      <li>
        <svg viewBox="0 0 10 10" aria-hidden="true"><rect x="0.5" y="2" width="9" height="6" fill="var(--orange)"/><path d="M0.5 2 L5 5.5 L9.5 2" fill="none" stroke="var(--card)" stroke-width="1"/></svg>
        sales@tailoredshield.com.au
      </li>
      <li>
        <svg viewBox="0 0 10 10" aria-hidden="true"><circle cx="5" cy="5" r="4.3" fill="none" stroke="var(--orange)" stroke-width="1.2"/><path d="M0.7 5 H9.3 M5 0.7 C2.5 3 2.5 7 5 9.3 M5 0.7 C7.5 3 7.5 7 5 9.3" fill="none" stroke="var(--orange)" stroke-width="0.9"/></svg>
        www.<span class="accent">tailoredshield</span>.com.au
      </li>
    </ul>
  </section>
</body>
</html>
```